Business Card and Stationary Designs for commercial construction company
Halvern Builders, Inc.
Creative Brief
Use standard fonts
Dennis Whitlock
Director of Operations
6387 Larkmeadow Lane Ashford, OR 95731
dennis.whitlock@halvernbldg.com
License #3084519
We like the colors of our logo, so please incorporate them into the card. The font for the other information on the business card does not have to match the logo font, but it should coordinate with it. We need the stationary design to be used to print actual stationary, but we would also like a word document that we can use for creating letters on electronic stationary.

```html
<!DOCTYPE html>
<html lang="en">
<head>
<meta charset="utf-8">
<title>Halvern Builders – Business Card</title>
<link href="https://fonts.googleapis.com/css2?family=Open+Sans:wght@400;600;800&display=swap" rel="stylesheet">
<style>
  :root {
    --brand-red: #e1252b;
    --brand-red-dark: #c81d23;
    --brand-grey: #8c8c8c;
    --ink: #333333;
    --paper: #ffffff;
    --backdrop: #e6e6e6;
  }
  * { box-sizing: border-box; margin: 0; padding: 0; }
  html, body { width: 1200px; height: 908px; overflow: hidden; }
  body {
    background: var(--backdrop);
    font-family: "Open Sans", Arial, sans-serif;
    position: relative;
  }
  .card {
    position: absolute;
    top: 304px;
    width: 520px;
    height: 300px;
    border-radius: 16px;
    overflow: hidden;
    box-shadow: 0 6px 18px rgba(0,0,0,0.18);
  }
  .card-front {
    left: 50px;
    background: linear-gradient(135deg, var(--brand-red) 0%, var(--brand-red-dark) 100%);
  }
  .front-decoration {
    position: absolute;
    right: 30px;
    top: 40px;
    width: 200px;
    height: 220px;
    background: rgba(255,255,255,0.08);
  }
  .front-brand {
    position: absolute;
    left: 50px;
    top: 132px;
    display: flex;
    align-items: center;
    gap: 12px;
  }
  .brand-mark {
    width: 30px;
    height: 30px;
    background: var(--paper);
  }
  .front-brand .brand-name {
    font-weight: 800;
    font-size: 34px;
    color: var(--paper);
    letter-spacing: 1px;
  }
  .card-back {
    left: 630px;
    background: var(--paper);
  }
  .back-wave { position: absolute; left: 0; top: 0; }
  .back-brand {
    position: absolute;
    right: 40px;
    top: 120px;
    display: flex;
    align-items: center;
    gap: 10px;
  }
  .back-brand .brand-mark { width: 24px; height: 24px; background: var(--brand-grey); }
  .back-brand .brand-name {
    font-weight: 800;
    font-size: 28px;
    color: var(--brand-red);
    letter-spacing: 1px;
  }
  .person {
    position: absolute;
    right: 40px;
    top: 166px;
    text-align: right;
  }
  .person-name { color: var(--brand-red); font-weight: 600; font-size: 15px; }
  .person-title { color: var(--ink); font-size: 11px; }
  .contact {
    position: absolute;
    left: 26px;
    top: 160px;
    font-size: 11px;
    line-height: 1.35;
    color: var(--ink);
  }
  .license { color: var(--brand-red); font-weight: 600; }
  .contact-line { display: flex; align-items: center; gap: 6px; margin-top: 1px; }
  .contact-icon { width: 12px; height: 12px; flex: none; }
</style>
</head>
<body>
  <section class="card card-front">
    <div class="front-decoration"></div>
    <div class="front-brand">
      <span class="brand-mark"></span>
      <span class="brand-name">HALVERN</span>
    </div>
  </section>

  <section class="card card-back">
    <svg class="back-wave" width="520" height="300" viewBox="0 0 520 300">
      <path d="M0,0 H520 V20 C420,60 300,130 0,118 Z" fill="var(--brand-red)"/>
      <path d="M0,130 C300,142 430,72 520,30" fill="none" stroke="var(--brand-grey)" stroke-width="7"/>
    </svg>
    <div class="back-brand">
      <span class="brand-mark"></span>
      <span class="brand-name">HALVERN</span>
    </div>
    <div class="person">
      <div class="person-name">Dennis Whitlock</div>
      <div class="person-title">Director of Operations</div>
    </div>
    <div class="contact">
      <div class="license">License #3084519</div>
      <div>6387 Larkmeadow Lane</div>
      <div>Ashford, OR 95731</div>
      <div class="contact-line">
        <svg class="contact-icon" viewBox="0 0 12 12"><circle cx="6" cy="6" r="6" fill="var(--brand-red)"/><path d="M4,3 L5,3 L5.6,4.6 L4.9,5.2 Q5.6,6.6 6.8,7.1 L7.4,6.4 L9,7 L9,8 Q6,9 3.5,4.5 Z" fill="#fff"/></svg>
        <span>541-555-0142</span>
      </div>
      <div class="contact-line">
        <svg class="contact-icon" viewBox="0 0 12 12"><circle cx="6" cy="6" r="6" fill="var(--brand-red)"/><rect x="4.2" y="2.6" width="3.6" height="6.8" rx="0.6" fill="#fff"/></svg>
        <span>541-555-0187</span>
      </div>
      <div class="contact-line">
        <svg class="contact-icon" viewBox="0 0 12 12"><circle cx="6" cy="6" r="6" fill="var(--brand-red)"/><rect x="3" y="4.5" width="6" height="3.5" fill="#fff"/><rect x="4" y="2.8" width="4" height="2" fill="#fff"/></svg>
        <span>541-555-0143</span>
      </div>
      <div class="contact-line">
        <svg class="contact-icon" viewBox="0 0 12 12"><circle cx="6" cy="6" r="6" fill="var(--brand-red)"/><rect x="3" y="3.8" width="6" height="4.4" fill="#fff"/><path d="M3,3.8 L6,6.3 L9,3.8" fill="none" stroke="var(--brand-red)" stroke-width="0.7"/></svg>
        <span>dennis.whitlock@halvernbldg.com</span>
      </div>
    </div>
  </section>
</body>
</html>
```